Revamp Marketing Website For Video Production Website

need to revamp current website www.quillhavenfilmworks.com
reference sites www.vandeo.com & http://layoutpike.com/quill/
Use all current content on current quill website. I want a revamped modenr look. Sometbing that wows customers.
reference site www.vandeo.com
Target Market(s)
business owners
Industry/Entity Type
Video Production
Number of Pages Required
5+ page
Colors
Designer to choose colors to be used in the design.
Requirements
Must have
- need to revamp current website www.quillhavenfilmworks.com
- reference sites www.vandeo.com & http://layoutpike.com/quill/
- Use all current content on current quill website. I want a revamped modenr look. Sometbing that wows customers.
- reference site www.vandeo.com
Nice to have
Should not have

```html
<!DOCTYPE html>
<html lang="en">
<head>
<meta charset="utf-8">
<title>Quill – Marketing Video Made for You</title>
<link href="https://fonts.googleapis.com/css2?family=Montserrat:wght@400;500;700&family=Roboto:wght@500;700&display=swap" rel="stylesheet">
<style>
  :root {
    --page-bg: #2f86e0;
    --hero-teal: #3aa3c9;
    --hero-blue: #3b49d6;
    --hero-indigo: #2a2582;
    --hero-night: #1b1752;
    --hero-violet: #5a3aa8;
    --ground: #ffffff;
    --text-light: #ffffff;
    --art-light: #dbe6fb;
    --art-blue: #4e7fd0;
    --art-pink: #d9409d;
  }
  html, body {
    margin: 0;
    width: 1200px;
    height: 1200px;
    overflow: hidden;
    background: var(--page-bg);
  }
  .landing {
    position: absolute;
    left: 0;
    top: 186px;
    width: 1200px;
    height: 829px;
    overflow: hidden;
    color: var(--text-light);
    background:
      radial-gradient(ellipse 70% 60% at 0% 0%, var(--hero-teal) 0%, rgba(58,163,201,0) 70%),
      radial-gradient(ellipse 60% 70% at 100% 0%, var(--hero-night) 0%, rgba(27,23,82,0) 75%),
      radial-gradient(ellipse 60% 60% at 100% 70%, var(--hero-violet) 0%, rgba(90,58,168,0) 70%),
      linear-gradient(160deg, var(--hero-indigo) 0%, var(--hero-blue) 100%);
  }
  .landing__ground {
    position: absolute;
    inset: 0;
    width: 1200px;
    height: 829px;
  }
  .brand {
    position: absolute;
    left: 95px;
    top: 66px;
    font-family: 'Montserrat', sans-serif;
  }
  .brand__name {
    display: block;
    font-weight: 700;
    font-size: 30px;
    letter-spacing: 8px;
    line-height: 30px;
  }
  .brand__tagline {
    display: block;
    font-weight: 700;
    font-size: 8.5px;
    letter-spacing: 0.4px;
    margin-top: 4px;
    opacity: 0.85;
  }
  .nav {
    position: absolute;
    top: 88px;
    left: 0;
    font-family: 'Montserrat', sans-serif;
    font-size: 18px;
  }
  .nav__link {
    position: absolute;
    white-space: nowrap;
    color: var(--text-light);
    text-decoration: none;
  }
  .nav__menu {
    position: absolute;
    left: 1091px;
    top: 90px;
    width: 24px;
    height: 20px;
  }
  .hero__title {
    position: absolute;
    left: 93px;
    top: 248px;
    margin: 0;
    font-family: 'Roboto', sans-serif;
    font-weight: 700;
    font-size: 57px;
    line-height: 55px;
    letter-spacing: -1px;
    white-space: nowrap;
  }
  .hero__text {
    position: absolute;
    left: 93px;
    top: 384px;
    width: 505px;
    margin: 0;
    font-family: 'Montserrat', sans-serif;
    font-size: 17.5px;
    line-height: 27px;
  }
  .hero__cta {
    position: absolute;
    left: 97px;
    top: 528px;
    width: 171px;
    height: 46px;
    box-sizing: border-box;
    border: 2px solid var(--text-light);
    border-radius: 6px;
    font-family: 'Roboto', sans-serif;
    font-weight: 500;
    font-size: 20px;
    line-height: 42px;
    text-align: center;
    color: var(--text-light);
    text-decoration: none;
  }
  .hero__art {
    position: absolute;
    left: 625px;
    top: 183px;
    width: 546px;
    height: 604px;
    border-radius: 24px;
    background: linear-gradient(150deg, var(--art-light) 0%, var(--art-blue) 60%, var(--art-pink) 100%);
    opacity: 0.9;
  }
</style>
</head>
<body>
  <main class="landing">
    <svg class="landing__ground" viewBox="0 0 1200 829" aria-hidden="true">
      <polygon points="0,730 620,560 0,760" fill="#4a3ce6" opacity="0.35"/>
      <polygon points="0,805 1200,490 1200,829 0,829" fill="var(--ground)"/>
    </svg>

    <div class="brand">
      <span class="brand__name">QUILL</span>
      <span class="brand__tagline">MARKETING VIDEOS MADE FOR YOU</span>
    </div>

    <nav class="nav">
      <a class="nav__link" href="#" style="left:505px">Home</a>
      <a class="nav__link" href="#" style="left:626px">Examples</a>
      <a class="nav__link" href="#" style="left:794px">FAQ</a>
      <a class="nav__link" href="#" style="left:920px">Contacts</a>
    </nav>
    <svg class="nav__menu" viewBox="0 0 24 20" aria-label="Menu" role="img">
      <rect x="0" y="1" width="24" height="2.4" fill="#fff"/>
      <rect x="0" y="9" width="24" height="2.4" fill="#fff"/>
      <rect x="0" y="17" width="24" height="2.4" fill="#fff"/>
    </svg>

    <h1 class="hero__title">Marketing Video<br>Made for You</h1>
    <p class="hero__text">Still using static image ads with Kinnect, Glimmer, Workbridge, Blinkchat advertising platforms? Turn them into VIDEO ADS and get higher conversion rates instantly.</p>
    <a class="hero__cta" href="#">Learn more</a>

    <div class="hero__art" role="img" aria-label="Isometric illustration: a large laptop showing a video player and bar charts, a film clapperboard, a person working on a small laptop, rising bar charts and floating chat and play icons"></div>
  </main>
</body>
</html>
```